Prospective Client Marketing Power Point Refresh/Update

My company has been using the attached power point to share with prospective clients. I'd like to have it refreshed with new graphics and style. The color pallet is something we'd like to stay true to. We are looking for your design expertise and ideas to help us update the look of the PP. We work with high wealth clients and want to have this reflect the value we can bring to the table.

Target Market(s)

Wealth Management Clients

Industry/Entity Type

Financial Advisors

Font styles to use
Sans Serif

Colors
0054AA
0677BA
7BADD7
CADEEF
E8F1F8
0094D4
00A9DD
6FCCEA
C7EBF8
E9F6FB

Requirements
Must have
• Updated look
Nice to have
• Fresh graphics

```html
<!DOCTYPE html>
<html lang="en">
<head>
<meta charset="utf-8">
<title>Brightline CFO – Client Presentation</title>
<link rel="stylesheet" href="https://fonts.googleapis.com/css2?family=Poppins:wght@400;500;600;700;800&display=swap">
<style>
:root{
  --navy:#0054AA;
  --blue:#0677BA;
  --sky:#0094D4;
  --bright:#00A9DD;
  --mist:#7BADD7;
  --ice:#C7EBF8;
  --pale:#E9F6FB;
  --paleblue:#E8F1F8;
  --bar:#1f9bd2;
  --ring:#2d9bd9;
  --ink:#1b1b1b;
  --text:#333a40;
  --green:#7a9e3f;
  --teal:#16a3a8;
  --canvas:#ececec;
  --slide:#fbfcfd;
}
*{box-sizing:border-box;margin:0;padding:0}
html,body{width:1200px;height:1065px;overflow:hidden}
body{background:var(--canvas);font-family:'Poppins',sans-serif;color:var(--text);position:relative}
.slide{position:absolute;width:531px;height:298px;background:var(--slide);overflow:hidden;box-shadow:0 3px 8px rgba(0,0,0,.18)}
.col-left{left:46px}.col-right{left:612px}
.row-1{top:61px}.row-2{top:378px}.row-3{top:719px}
.abs{position:absolute}
.slide-title{position:absolute;left:11px;top:12px;font-size:17.5px;font-weight:700;color:var(--blue);letter-spacing:-.1px;white-space:nowrap}
.brand{position:absolute;font-family:'Poppins',sans-serif;font-weight:600;color:var(--blue);white-space:nowrap;line-height:1}
.brand-small{right:12px;top:16px;font-size:11px}
.footer{position:absolute;left:0;right:0;bottom:0;height:25px;background:var(--bar);color:#fff;font-size:12.5px;display:flex;align-items:center;justify-content:space-between;padding:0 11px}
.footer .num{font-size:12px}
.body{font-size:6.3px;line-height:1.42;color:var(--text)}
.sub{font-size:9.6px;font-weight:600;color:var(--blue);white-space:nowrap}
.photo{position:absolute;border-radius:50%}
/* slide 1 */
.cover-top{position:absolute;left:232px;right:0;top:0;height:25px;background:var(--bar)}
.cover-bottom{position:absolute;left:232px;right:0;bottom:0;height:25px;background:var(--bar);color:#fff;font-size:11.5px;letter-spacing:2px;text-align:right;padding:5px 11px 0 0}
.cover-title{right:11px;top:168px;text-align:right;font-size:28px;font-weight:800;color:var(--ink);line-height:1.2;letter-spacing:.3px}
/* slide 2 */
.point{position:absolute;width:146px}
.point.left{left:10px;text-align:right}
.point.right{left:377px}
.icon{position:absolute;width:23px;height:23px}
.callout{position:absolute;left:134px;width:257px;top:244px;height:32px;background:var(--bar);border-radius:8px 8px 0 0;color:#fff;font-size:7.2px;line-height:1.35;text-align:center;padding:4px 8px 0}
/* slide 3 */
.expertise{position:absolute;left:0;top:83px;width:207px;height:120px;background:var(--bar);border-radius:0 8px 8px 0;color:#fff;font-size:13.6px;font-weight:600;line-height:1.37;padding:16px 10px 0 11px}
.service{position:absolute;font-size:6.8px;line-height:1.35;color:var(--text);white-space:nowrap}
/* slide 4 */
.flow{position:absolute;top:120px;height:48px;border-radius:6px;color:#fff;text-align:center;display:flex;flex-direction:column;justify-content:center;font-weight:600}
/* slide 5 */
.panel{position:absolute}
/* slide 6 */
.thanks{left:20px;top:130px;width:255px;text-align:center;color:#fff;font-size:31px;font-weight:800;letter-spacing:.5px;text-shadow:0 1px 3px rgba(0,0,0,.25)}
.contact{position:absolute;right:28px;font-size:10.5px;color:var(--ink);text-align:right;line-height:1.2;white-space:nowrap}
.contact-icon{position:absolute;right:11px;width:10px;height:10px}
</style>
</head>
<body>

<!-- Cover -->
<section class="slide col-left row-1 cover">
  <div class="cover-top"></div>
  <svg class="abs" style="left:0;top:0" width="300" height="298" viewBox="0 0 300 298">
    <circle cx="147" cy="148" r="147" fill="var(--blue)"/>
    <circle cx="147" cy="148" r="130" fill="var(--ring)"/>
  </svg>
  <div class="photo" role="img" aria-label="City skyline with a suspension bridge reflected in the river" style="left:35px;top:36px;width:224px;height:224px;background:linear-gradient(180deg,#d9dfe3 0%,#b8c2ca 45%,#5d6f82 62%,#8a9aab 80%,#c3ccd4 100%)"></div>
  <div class="brand" style="right:20px;top:96px;font-size:26px">Brightline CFO</div>
  <div class="abs cover-title">PRESENTATION<br>TITLE</div>
  <div class="cover-bottom">www.brightlinecfo.com</div>
</section>

<!-- Relationship -->
<section class="slide col-right row-1">
  <h1 class="slide-title">The Brightline CFO Relationship</h1>
  <div class="brand brand-small">Brightline CFO</div>

  <svg class="icon" style="left:133px;top:52px" viewBox="0 0 24 24"><circle cx="12" cy="12" r="11" fill="none" stroke="var(--bar)" stroke-width="1"/><text x="12" y="15.5" font-size="10" text-anchor="middle" fill="var(--bar)" font-family="Poppins,sans-serif">$</text></svg>
  <p class="point left body" style="top:78px">Providing the highest level of wealth advisory services.</p>
  <svg class="icon" style="left:133px;top:104px" viewBox="0 0 24 24"><circle cx="12" cy="12" r="11" fill="none" stroke="var(--bar)" stroke-width="1"/><rect x="7.5" y="7" width="9" height="10" fill="none" stroke="var(--bar)" stroke-width="1"/><path d="M9 10h6M9 12.5h6M9 15h4" stroke="var(--bar)" stroke-width=".8"/></svg>
  <p class="point left body" style="top:127px">There are so many financial decisions that impact multiple areas of an individual's balance sheet exposing you to a potentially costly mistake.</p>
  <svg class="icon" style="left:133px;top:176px" viewBox="0 0 24 24"><circle cx="12" cy="12" r="11" fill="none" stroke="var(--bar)" stroke-width="1"/><path d="M12 5.5l5 2v4c0 3.2-2.2 5.6-5 6.6-2.8-1-5-3.4-5-6.6v-4z" fill="none" stroke="var(--bar)" stroke-width="1"/><path d="M9.5 12l1.8 1.8 3.3-3.5" fill="none" stroke="var(--bar)" stroke-width="1"/></svg>
  <p class="point left body" style="top:200px">As an independent Registered Investment Advisor, we follow the highest financial standards.</p>

  <svg class="abs" style="left:183px;top:54px" width="170" height="170" viewBox="0 0 170 170">
    <circle cx="85" cy="85" r="85" fill="var(--blue)"/>
    <circle cx="85" cy="85" r="75" fill="var(--ring)"/>
  </svg>
  <div class="photo" role="img" aria-label="Advisor and client in conversation at a table by a bright window" style="left:206px;top:77px;width:124px;height:124px;background:linear-gradient(135deg,#e8ecef 0%,#c9d2d8 45%,#7f8c95 70%,#dfe4e8 100%)"></div>

  <svg class="icon" style="left:377px;top:52px" viewBox="0 0 24 24"><circle cx="12" cy="12" r="11" fill="none" stroke="var(--bar)" stroke-width="1"/><path d="M6 12l3-3 3 2 3-2 3 3-4 4-2-1-2 1z" fill="none" stroke="var(--bar)" stroke-width="1"/></svg>
  <p class="point right body" style="top:78px">We love being a trusted advisor to deliver exceptional service.</p>
  <svg class="icon" style="left:377px;top:104px" viewBox="0 0 24 24"><circle cx="12" cy="12" r="11" fill="none" stroke="var(--bar)" stroke-width="1"/><circle cx="12" cy="12" r="6" fill="none" stroke="var(--bar)" stroke-width="1"/><circle cx="12" cy="12" r="3" fill="none" stroke="var(--bar)" stroke-width="1"/><path d="M12 12l5-5" stroke="var(--bar)" stroke-width="1"/></svg>
  <p class="point right body" style="top:127px">Our goal is to give you the peace of mind that all aspects of your financial picture are being taken care of.</p>
  <svg class="icon" style="left:377px;top:176px" viewBox="0 0 24 24"><circle cx="12" cy="12" r="11" fill="none" stroke="var(--bar)" stroke-width="1"/><text x="12" y="16" font-size="12" text-anchor="middle" fill="var(--bar)" font-family="Poppins,sans-serif">$</text></svg>
  <p class="point right body" style="top:200px;width:145px">We work on a fee-only basis and do not sell commission-based or proprietary products or receive kickbacks of any kind.</p>

  <div class="callout">This gives us the freedom to develop your financial plan and investment strategy without biased outside influences.</div>
  <div class="footer"><span>www.brightlinecfo.com</span><span class="num">01</span></div>
</section>

<!-- Services -->
<section class="slide col-left row-2">
  <h1 class="slide-title">What Do We Do?</h1>
  <div class="brand brand-small">Brightline CFO</div>
  <div class="expertise">We Have The Expertise And Experience To Provide An Exceptional Personal CFO Relationship.</div>

  <svg class="abs" style="left:291px;top:68px" width="170" height="170" viewBox="0 0 170 170">
    <circle cx="85" cy="85" r="62" fill="var(--blue)"/>
    <circle cx="85" cy="85" r="55" fill="var(--ring)"/>
    <circle cx="85" cy="85" r="45" fill="#fff"/>
    <g fill="#fff" stroke="var(--ring)" stroke-width="1.6">
      <circle cx="85" cy="12" r="8.5"/><circle cx="137" cy="33" r="8.5"/>
      <circle cx="158" cy="85" r="8.5"/><circle cx="137" cy="137" r="8.5"/>
      <circle cx="85" cy="158" r="8.5"/><circle cx="33" cy="137" r="8.5"/>
      <circle cx="12" cy="85" r="8.5"/><circle cx="33" cy="33" r="8.5"/>
    </g>
    <g fill="none" stroke="var(--blue)" stroke-width=".8">
      <path d="M81 15l3-3 2 2 3-4"/>
      <rect x="133" y="30" width="8" height="6"/>
      <path d="M154 89v-5l4-3 4 3v5z"/>
      <path d="M133 139h8M135 136h4"/>
      <rect x="82" y="154" width="6" height="8"/>
      <path d="M30 138c1-3 5-3 6 0"/>
      <circle cx="12" cy="85" r="3"/>
      <path d="M30 30h6v6h-6z"/>
    </g>
    <text x="85" y="89" text-anchor="middle" font-family="Poppins,sans-serif" font-size="11" font-weight="600" fill="var(--blue)">Brightline CFO</text>
  </svg>

  <p class="service" style="left:356px;top:46px;text-align:center">Investment<br>Management</p>
  <p class="service" style="left:444px;top:94px">Executive<br>Compensation<br>&amp; Benefits</p>
  <p class="service" style="left:460px;top:147px">Retirement<br>Planning</p>
  <p class="service" style="left:456px;top:200px">Education</p>
  <p class="service" style="left:359px;top:236px">Insurance</p>
  <p class="service" style="left:254px;top:200px">Philanthropy</p>
  <p class="service" style="left:222px;top:147px;text-align:right">Cash Management<br>&amp; Budgeting</p>
  <p class="service" style="left:246px;top:92px;text-align:right">Tax Planning &amp;<br>Compliance</p>

  <div class="footer"><span>www.brightlinecfo.com</span><span class="num">02</span></div>
</section>

<!-- Philosophy -->
<section class="slide col-right row-2">
  <h1 class="slide-title">Guiding Investment Philosophy</h1>
  <div class="brand brand-small">Brightline CFO</div>

  <h2 class="sub abs" style="left:11px;top:56px">Embrace Market Pricing</h2>
  <p class="body abs" style="left:11px;top:75px;width:246px">The market is an effective information-processing machine. Each day, the world equity markets process billions of dollars in trades between buyers and sellers – and the real-time information they bring helps set prices.</p>

  <div class="flow" style="left:31px;width:53px;background:#1a6d9e;font-size:6.4px;line-height:1.4">ALL<br>AVAILABLE<br>INFORMATION</div>
  <svg class="abs" style="left:84px;top:138px" width="10" height="12"><path d="M1 1l6 5-6 5" fill="none" stroke="#5fb0a0" stroke-width="1.5"/></svg>
  <div class="flow" style="left:94px;width:53px;background:#1ea6a2"><span style="font-size:10.5px;font-weight:700">$462.8B</span><span style="font-size:4.6px;font-weight:400;line-height:1.3">World Equity<br>Trading in 2018<br>(Daily Average)</span></div>
  <svg class="abs" style="left:147px;top:138px" width="10" height="12"><path d="M1 1l6 5-6 5" fill="none" stroke="#8cb36a" stroke-width="1.5"/></svg>
  <div class="flow" style="left:168px;width:53px;background:#8fab57;font-size:10.5px;font-weight:700">PRICES</div>

  <h2 class="sub abs" style="left:11px;top:178px">Don't Try to Outguess the Market</h2>
  <p class="body abs" style="left:11px;top:197px;width:246px;text-align:justify">The market's pricing power works against mutual fund managers who try to outperform through stock pricing or market timing. As evidence, only 23% of US equity mutual funds and 8% of fixed income funds have survived and outperformed their benchmarks over the past 20 years.</p>

  <h2 class="sub abs" style="left:282px;top:56px">Resist Chasing Past Performance</h2>
  <p class="body abs" style="left:282px;top:75px;width:240px">Some investors select mutual funds based on their past returns. Yet, past performance offers little insight into a fund's future returns. For example, most funds in the top quartile (25%) of previous five-year returns did not maintain a top-quartile ranking in the following five years.</p>

  <svg class="abs" style="left:294px;top:124px" width="210" height="142" viewBox="0 0 210 142">
    <text x="105" y="8" text-anchor="middle" font-family="Poppins,sans-serif" font-size="5.8" fill="#333">Percentage of Top-Ranked Funds That Stayed on Top</text>
    <line x1="2" y1="13" x2="195" y2="13" stroke="#555" stroke-width=".5"/>
    <rect x="7" y="18" width="40" height="28" fill="#3b72c0"/>
    <text x="27" y="30" text-anchor="middle" font-family="Poppins,sans-serif" font-size="7.5" font-weight="700" fill="#fff">TOP 25</text>
    <text x="27" y="39" text-anchor="middle" font-family="Poppins,sans-serif" font-size="7.5" font-weight="700" fill="#fff">%</text>
    <rect x="7" y="47" width="40" height="18" fill="#c9d8ef"/>
    <rect x="7" y="66" width="40" height="24" fill="#dfe8f5"/>
    <rect x="7" y="91" width="40" height="24" fill="#c9d8ef"/>
    <text x="27" y="125" text-anchor="middle" font-family="Poppins,sans-serif" font-size="5.6" fill="#333">Previous</text>
    <text x="27" y="132" text-anchor="middle" font-family="Poppins,sans-serif" font-size="5.6" fill="#333">5 Years</text>
    <path d="M47 18L71 48M47 46L71 90" stroke="#555" stroke-width=".5" fill="none"/>
    <path d="M62 28v20h9M62 70v20h9" stroke="#555" stroke-width=".5" fill="none"/>
    <rect x="71" y="25" width="124" height="17" fill="#d7d7d7"/>
    <text x="191" y="37" text-anchor="end" font-family="Poppins,sans-serif" font-size="7.5" fill="#7a9e3f">Equity</text>
    <rect x="71" y="40" width="24" height="16" fill="#16a3b8"/>
    <text x="83" y="52" text-anchor="middle" font-family="Poppins,sans-serif" font-size="10" font-weight="700" fill="#fff">21%</text>
    <rect x="71" y="65" width="124" height="16" fill="#d7d7d7"/>
    <text x="191" y="76" text-anchor="end" font-family="Poppins,sans-serif" font-size="7.5" fill="#7a9e3f">Fixed Income</text>
    <rect x="71" y="81" width="34" height="17" fill="#6c9a2e"/>
    <text x="88" y="93" text-anchor="middle" font-family="Poppins,sans-serif" font-size="10" font-weight="700" fill="#fff">28%</text>
    <text x="172" y="94" text-anchor="middle" font-family="Poppins,sans-serif" font-size="7.5" font-weight="600" fill="#222">100%</text>
    <text x="66" y="114" font-family="Poppins,sans-serif" font-size="5.4" fill="#333">Funds Remaining in Top Quartile of Returns</text>
    <text x="66" y="121" font-family="Poppins,sans-serif" font-size="5.4" fill="#333">in the Following 5-Year Period (2008–2018</text>
    <text x="66" y="128" font-family="Poppins,sans-serif" font-size="5.4" fill="#333">average)</text>
  </svg>

  <div class="footer"><span>www.brightlinecfo.com</span><span class="num">03</span></div>
</section>

<!-- Efficient markets -->
<section class="slide col-left row-3">
  <h1 class="slide-title">The Power of Efficient Markets</h1>
  <div class="brand brand-small">Brightline CFO</div>

  <div class="panel" style="left:0;top:52px;width:247px;height:215px;background:var(--pale)"></div>
  <h2 class="sub abs" style="left:11px;top:58px">Let Markets Work for You</h2>
  <p class="body abs" style="left:11px;top:75px;width:225px;text-align:justify">The financial markets have rewarded long-term investors. People expect a positive return on the capital they supply, and historically, the equity and bond markets have provided growth of wealth that has more then offset inflation.</p>
  <svg class="abs" style="left:46px;top:117px" width="138" height="74" viewBox="0 0 138 74">
    <rect width="138" height="74" fill="#fff"/>
    <text x="3" y="6" font-family="Poppins,sans-serif" font-size="3.4" fill="#555">Growth of a Dollar, 1926–2018</text>
    <path d="M6 68L20 60 35 56 50 48 65 40 80 30 95 22 108 12 118 7 118 68z" fill="#2a96b8"/>
    <path d="M6 68L20 62 35 60 50 54 65 48 80 40 95 34 108 28 118 24 118 68z" fill="#8fc6d6"/>
    <path d="M6 68L30 64 55 60 80 54 100 48 118 42 118 68z" fill="#7aa63a"/>
    <path d="M6 68L40 66 80 62 118 58 118 68z" fill="#b9cf8f"/>
    <path d="M6 68h112" stroke="#444" stroke-width=".4"/>
    <g font-family="Poppins,sans-serif" font-size="2.6" fill="#444">
      <text x="120" y="8">Small Cap</text><text x="120" y="24">Large Cap</text>
      <text x="120" y="42">Bonds</text><text x="120" y="52">Bills</text><text x="120" y="60">Inflation</text>
    </g>
  </svg>
  <h2 class="sub abs" style="left:11px;top:202px">Consider the Drivers of Returns</h2>
  <p class="body abs" style="left:11px;top:220px;width:225px;text-align:justify">There is a wealth of academic research into what drives returns. Expected returns depend on current market prices and expected future cash flows. Investors can use this information to pursue higher expected returns in their portfolios.</p>

  <div class="panel" style="left:257px;top:52px;width:274px;height:103px;background:var(--paleblue)"></div>
  <h2 class="sub abs" style="left:266px;top:58px">Avoid Market Timing</h2>
  <p class="body abs" style="left:266px;top:75px;width:145px;text-align:justify">You never know which market segments will out perform from year to year. By holding a globally diversified portfolio, investors are well positioned to seek returns wherever they occur.</p>
  <svg class="abs" style="left:417px;top:59px" width="103" height="86" viewBox="0 0 103 86">
    <rect width="103" height="86" fill="#fff"/>
    <text x="51.5" y="8" text-anchor="middle" font-family="Poppins,sans-serif" font-size="3.8" font-weight="600" fill="#333" text-decoration="underline">Dimensions of Expected Returns</text>
    <text x="4" y="15" font-family="Poppins,sans-serif" font-size="2.6" fill="#1a8fb8">EQUITIES</text>
    <g fill="#1a9ec4"><rect x="4" y="18" width="94" height="6"/><rect x="4" y="25" width="94" height="6"/><rect x="4" y="32" width="94" height="6"/></g>
    <text x="4" y="53" font-family="Poppins,sans-serif" font-size="2.6" fill="#6c9a2e">FIXED INCOME</text>
    <g fill="#6c9a2e"><rect x="4" y="56" width="94" height="6"/><rect x="4" y="63" width="94" height="6"/><rect x="4" y="70" width="94" height="6"/></g>
    <g font-family="Poppins,sans-serif" font-size="2.6" fill="#fff">
      <text x="6" y="22.2">Company Size</text><text x="6" y="29.2">Relative Price</text><text x="6" y="36.2">Profitability</text>
      <text x="6" y="60.2">Term</text><text x="6" y="67.2">Credit</text><text x="6" y="74.2">Currency</text>
    </g>
  </svg>

  <div class="panel" style="left:257px;top:167px;width:274px;height:100px;background:var(--paleblue)"></div>
  <h2 class="sub abs" style="left:266px;top:179px">Practice Smart Diversification</h2>
  <p class="body abs" style="left:266px;top:197px;width:140px;text-align:justify">Holding securities across many market segments can help manage overall risk. But diversifying within your home market may not be enough. Global diversification can broaden your investment universe.</p>
  <svg class="abs" style="left:414px;top:182px" width="106" height="61" viewBox="0 0 106 61">
    <rect width="106" height="61" fill="#fff"/>
    <g stroke="#999" stroke-width=".4"><path d="M5 6h14M5 14h14M5 22h14M5 30h14M5 38h14M5 46h14M5 54h14"/></g>
    <g id="heat">
      <rect x="33" y="8" width="8" height="6" fill="#2f86c6"/><rect x="41" y="8" width="8" height="6" fill="#9bcf5b"/><rect x="49" y="8" width="8" height="6" fill="#3fb2c4"/><rect x="57" y="8" width="8" height="6" fill="#b7b7b7"/><rect x="65" y="8" width="8" height="6" fill="#4f9e3d"/><rect x="73" y="8" width="8" height="6" fill="#2f86c6"/><rect x="81" y="8" width="8" height="6" fill="#7fc5e0"/><rect x="89" y="8" width="8" height="6" fill="#5f7fbf"/>
      <rect x="33" y="14" width="8" height="6" fill="#7fc5e0"/><rect x="41" y="14" width="8" height="6" fill="#2f86c6"/><rect x="49" y="14" width="8" height="6" fill="#9a9a9a"/><rect x="57" y="14" width="8" height="6" fill="#9bcf5b"/><rect x="65" y="14" width="8" height="6" fill="#3fb2c4"/><rect x="73" y="14" width="8" height="6" fill="#d0d0d0"/><rect x="81" y="14" width="8" height="6" fill="#4f9e3d"/><rect x="89" y="14" width="8" height="6" fill="#2f86c6"/>
      <rect x="33" y="20" width="8" height="6" fill="#4f9e3d"/><rect x="41" y="20" width="8" height="6" fill="#3fb2c4"/><rect x="49" y="20" width="8" height="6" fill="#2f86c6"/><rect x="57" y="20" width="8" height="6" fill="#7fc5e0"/><rect x="65" y="20" width="8" height="6" fill="#b7b7b7"/><rect x="73" y="20" width="8" height="6" fill="#9bcf5b"/><rect x="81" y="20" width="8" height="6" fill="#5f7fbf"/><rect x="89" y="20" width="8" height="6" fill="#3fb2c4"/>
      <rect x="33" y="26" width="8" height="6" fill="#d0d0d0"/><rect x="41" y="26" width="8" height="6" fill="#5f7fbf"/><rect x="49" y="26" width="8" height="6" fill="#9bcf5b"/><rect x="57" y="26" width="8" height="6" fill="#2f86c6"/><rect x="65" y="26" width="8" height="6" fill="#7fc5e0"/><rect x="73" y="26" width="8" height="6" fill="#4f9e3d"/><rect x="81" y="26" width="8" height="6" fill="#9a9a9a"/><rect x="89" y="26" width="8" height="6" fill="#9bcf5b"/>
      <rect x="33" y="32" width="8" height="6" fill="#3fb2c4"/><rect x="41" y="32" width="8" height="6" fill="#b7b7b7"/><rect x="49" y="32" width="8" height="6" fill="#4f9e3d"/><rect x="57" y="32" width="8" height="6" fill="#3fb2c4"/><rect x="65" y="32" width="8" height="6" fill="#2f86c6"/><rect x="73" y="32" width="8" height="6" fill="#7fc5e0"/><rect x="81" y="32" width="8" height="6" fill="#9bcf5b"/><rect x="89" y="32" width="8" height="6" fill="#d0d0d0"/>
      <rect x="33" y="38" width="8" height="6" fill="#9bcf5b"/><rect x="41" y="38" width="8" height="6" fill="#d0d0d0"/><rect x="49" y="38" width="8" height="6" fill="#5f7fbf"/><rect x="57" y="38" width="8" height="6" fill="#4f9e3d"/><rect x="65" y="38" width="8" height="6" fill="#9a9a9a"/><rect x="73" y="38" width="8" height="6" fill="#3fb2c4"/><rect x="81" y="38" width="8" height="6" fill="#2f86c6"/><rect x="89" y="38" width="8" height="6" fill="#7fc5e0"/>
      <rect x="33" y="44" width="8" height="6" fill="#b7b7b7"/><rect x="41" y="44" width="8" height="6" fill="#7fc5e0"/><rect x="49" y="44" width="8" height="6" fill="#d0d0d0"/><rect x="57" y="44" width="8" height="6" fill="#5f7fbf"/><rect x="65" y="44" width="8" height="6" fill="#4f9e3d"/><rect x="73" y="44" width="8" height="6" fill="#b7b7b7"/><rect x="81" y="44" width="8" height="6" fill="#3fb2c4"/><rect x="89" y="44" width="8" height="6" fill="#9bcf5b"/>
      <rect x="33" y="50" width="8" height="6" fill="#9a9a9a"/><rect x="41" y="50" width="8" height="6" fill="#9bcf5b"/><rect x="49" y="50" width="8" height="6" fill="#7fc5e0"/><rect x="57" y="50" width="8" height="6" fill="#d0d0d0"/><rect x="65" y="50" width="8" height="6" fill="#5f7fbf"/><rect x="73" y="50" width="8" height="6" fill="#9a9a9a"/><rect x="81" y="50" width="8" height="6" fill="#b7b7b7"/><rect x="89" y="50" width="8" height="6" fill="#4f9e3d"/>
    </g>
    <path d="M25 8v48" stroke="#666" stroke-width=".4"/>
  </svg>
  <p class="abs" style="right:11px;top:256px;font-size:6.4px;color:#333">Source: Northfield Data</p>

  <div class="footer"><span>www.brightlinecfo.com</span><span class="num">04</span></div>
</section>

<!-- Closing -->
<section class="slide col-right row-3">
  <div class="cover-top" style="left:234px;height:26px"></div>
  <div class="abs" style="left:234px;right:0;bottom:0;height:25px;background:var(--bar)"></div>
  <svg class="abs" style="left:0;top:0" width="300" height="298" viewBox="0 0 300 298">
    <circle cx="147" cy="151" r="148" fill="var(--blue)"/>
    <circle cx="147" cy="151" r="138" fill="var(--ring)"/>
  </svg>
  <div class="photo" role="img" aria-label="Family walking hand in hand along a beach at the water's edge" style="left:22px;top:26px;width:250px;height:250px;background:linear-gradient(180deg,#9fc3d8 0%,#7fa9c3 40%,#6d97b0 60%,#a9c3cf 85%,#c7d6dc 100%)"></div>
  <div class="abs thanks">THANK YOU!</div>

  <div class="brand" style="right:12px;top:116px;font-size:24px">Brightline CFO</div>

  <p class="contact" style="top:185px">555 014 2090</p>
  <svg class="contact-icon" style="top:187px" viewBox="0 0 10 10"><circle cx="5" cy="5" r="5" fill="var(--ink)"/><path d="M3.2 2.8c0 2.3 1.7 4 4 4l.4-1-1-.6-.6.5c-.8-.4-1.3-.9-1.7-1.7l.5-.6-.6-1z" fill="#fff"/></svg>
  <p class="contact" style="top:203px">www.brightlinecfo.com</p>
  <svg class="contact-icon" style="top:205px" viewBox="0 0 10 10"><circle cx="5" cy="5" r="4.3" fill="none" stroke="var(--ink)" stroke-width="1"/><path d="M1 5h8M5 .8c-2 2.6-2 5.8 0 8.4M5 .8c2 2.6 2 5.8 0 8.4" fill="none" stroke="var(--ink)" stroke-width=".7"/></svg>
  <p class="contact" style="top:221px">480 Harbor Avenue, Suite 210<br>Riverton, WA 98000</p>
  <svg class="contact-icon" style="top:223px" viewBox="0 0 10 10"><circle cx="5" cy="5" r="5" fill="var(--ink)"/><path d="M5 2.2a1.9 1.9 0 0 0-1.9 1.9c0 1.5 1.9 3.6 1.9 3.6s1.9-2.1 1.9-3.6A1.9 1.9 0 0 0 5 2.2z" fill="#fff"/><circle cx="5" cy="4.1" r=".7" fill="var(--ink)"/></svg>
  <p class="contact" style="top:251px">555 014 6205</p>
  <svg class="contact-icon" style="top:253px" viewBox="0 0 10 10"><circle cx="5" cy="5" r="5" fill="var(--ink)"/><rect x="2.5" y="4" width="5" height="3" fill="#fff"/><rect x="3.5" y="2.5" width="3" height="1.5" fill="#fff"/></svg>
</section>

</body>
</html>
```